Business Card Design Project

We need a Business Card for an Mechanical Engineering firm in Singapore. The design should be Modern & Technical looking, yet eye catching.

Our company deals in Cutting Tools & Machine Accessories for the Manufacturing Industries such as Oil & Gas, Aero Space, etc... For more information on our Company, you can either email me or view our website www.valtrion.com.sg.

We are trying to revamp our image to give our consumers a fresh new perspective to our company, so we welcome all ideas.

Industry/Entity Type

Business

Requirements
Must have
• Must incorporate New Company Logo into the card as shown in Uploaded file.

```html
<!DOCTYPE html>
<html lang="en">
<head>
<meta charset="utf-8">
<title>Valtrion Tools – Business Card</title>
<link rel="stylesheet" href="https://fonts.googleapis.com/css2?family=Source+Sans+3:wght@400;600;700&display=swap">
<style>
  :root {
    --backdrop: #e6e6e6;
    --card: #fbfafa;
    --brand: #9c1240;
    --brand-faint: #ecd3dc;
    --ink: #1c1c1c;
    --muted: #7d7d7d;
    --soft: #9a9a9a;
  }
  * { margin: 0; padding: 0; box-sizing: border-box; }
  html, body { width: 1200px; height: 900px; overflow: hidden; }
  body {
    background: var(--backdrop);
    font-family: "Source Sans 3", "Myriad Pro", Arial, sans-serif;
    position: relative;
  }
  .card {
    position: absolute;
    left: 300px;
    width: 600px;
    height: 345px;
    background: var(--card);
    box-shadow: 0 6px 18px rgba(0,0,0,0.18);
  }
  .card--front { top: 70px; }
  .card--back { top: 485px; }

  /* Front: brand name */
  .brand-lockup {
    position: absolute;
    inset: 0;
    display: flex;
    align-items: center;
    justify-content: center;
    gap: 16px;
  }
  .brand-dot {
    width: 34px; height: 34px;
    border-radius: 50%;
    background: var(--brand);
  }
  .brand-name {
    color: var(--brand);
    font-weight: 700;
    font-size: 48px;
    letter-spacing: 1px;
    text-transform: uppercase;
  }

  /* Back: contact details */
  .person {
    position: absolute;
    left: 44px; top: 34px;
    display: flex;
    align-items: flex-end;
    gap: 18px;
  }
  .person__name { font-size: 36px; font-weight: 400; color: var(--ink); line-height: 1; }
  .person__name .surname { color: var(--muted); }
  .person__role { color: var(--brand); font-size: 19px; font-weight: 400; margin-bottom: -16px; }
  .contact {
    position: absolute; left: 44px; top: 82px;
    color: var(--soft);
  }
  .contact__phone { font-size: 21px; line-height: 1.1; }
  .contact__email { font-size: 16px; line-height: 1.3; }
  .address {
    position: absolute; left: 44px; top: 166px;
    color: var(--soft);
    font-style: normal;
    font-size: 15px;
    line-height: 1.35;
  }
  .address__company { font-weight: 700; color: var(--muted); }
  .website {
    position: absolute; left: 44px; top: 262px;
    color: var(--brand); font-size: 16px;
  }
  .mark-area {
    position: absolute;
    right: 0; bottom: 0;
    width: 330px; height: 200px;
  }
</style>
</head>
<body>
  <section class="card card--front" aria-label="Card front">
    <div class="brand-lockup">
      <span class="brand-dot"></span>
      <span class="brand-name">Valtrion Tools</span>
    </div>
  </section>

  <section class="card card--back" aria-label="Card back">
    <div class="person">
      <h1 class="person__name">Mark <span class="surname">Dalton</span></h1>
      <p class="person__role">PRESIDENT &amp; CEO</p>
    </div>
    <div class="contact">
      <p class="contact__phone">+65-6123 4567</p>
      <p class="contact__email">mark@valtrion.com.sg</p>
    </div>
    <address class="address">
      <span class="address__company">Valtrion Tools Pte Ltd</span><br>
      27 Kallang Way #03-12,<br>
      Meridian Industrial Park,<br>
      Singapore 349210
    </address>
    <p class="website">www.valtrion.com.sg</p>
    <svg class="mark-area" viewBox="0 0 330 200" role="img" aria-label="Faint brand mark decoration area">
      <defs>
        <linearGradient id="mark-fade" x1="0" y1="1" x2="1" y2="0">
          <stop offset="0" stop-color="#ecd3dc" stop-opacity="0.9"/>
          <stop offset="1" stop-color="#ecd3dc" stop-opacity="0.3"/>
        </linearGradient>
      </defs>
      <rect x="0" y="0" width="330" height="200" fill="url(#mark-fade)"/>
    </svg>
  </section>
</body>
</html>
```